Music Business Adviser Needs a Book Cover Design

I need a cover design for my new book called 'The Stage Performer: A Working Handbook for Launching Your Trade'. I am an accountant and tax lawyer specialising in advising international music artists. This book is designed to help music artists and bands navigate through the business world. I would like to see designs that would appeal to young artists, the book needs to be bold and stand out from the crowd, for example it will attract people on Bookvale through its enticing cover.

I am open to you providing creative input on the design, although I like the colour green and think this would perhaps communicate subtly financial safety and growth. The cover should clearly communicate the book is for people in the music industry.

Target Market(s)

Males and females aged between 16 and 30; their hobbies and interest are music; they perform and record music; all genres of music

Industry/Entity Type

Lawyer

Font styles to use
Sans Serif

Requirements
Must have
• Must have the title clearly stated: 'The Stage Performer: A Working Handbook for Launching Your Trade'. It must also have my name as author on the front: 'Gareth L. Quinby'
Nice to have
• I have uploaded an image of the type of artwork, that should be on the book. I like this style - so please keep it simple, not an over complicated design.
Should not have
• Photographs of bands or musicians

```html
<!DOCTYPE html>
<html lang="en">
<head>
<meta charset="utf-8">
<title>The Stage Performer – Book Cover</title>
<link rel="stylesheet" href="https://fonts.googleapis.com/css2?family=Anton&family=Montserrat:wght@300;400;700;800&display=swap">
<style>
  :root {
    --canvas-bg: #ececec;
    --green-deep: #3d761c;
    --green-mid: #5c9a2a;
    --green-light: #9fce4a;
    --spine-green: #356a18;
    --bulb-yellow: #f2e600;
    --ink-dark: #1f2a12;
    --paper: #ffffff;
  }
  * { margin: 0; padding: 0; box-sizing: border-box; }
  html, body { width: 1200px; height: 1200px; overflow: hidden; }
  body {
    background: var(--canvas-bg);
    font-family: "Montserrat", sans-serif;
  }
  .cover-wrap {
    position: absolute;
    left: 62px;
    top: 230px;
    width: 1076px;
    height: 740px;
    display: flex;
    box-shadow: 0 18px 40px rgba(0,0,0,0.18);
  }

  /* Back cover */
  .back-cover {
    position: relative;
    width: 520px;
    height: 100%;
    background: var(--green-mid);
    color: var(--paper);
    overflow: hidden;
  }
  .publisher-mark {
    position: absolute;
    top: 48px;
    right: 44px;
    display: flex;
    align-items: center;
    gap: 10px;
  }
  .publisher-square {
    width: 14px;
    height: 14px;
    background: var(--paper);
  }
  .publisher-name {
    font-family: "Montserrat", sans-serif;
    font-weight: 300;
    font-size: 18px;
    color: var(--paper);
  }
  .blurb {
    position: absolute;
    top: 150px;
    left: 50px;
    right: 50px;
    font-size: 13px;
    font-weight: 300;
    line-height: 1.6;
    text-align: center;
  }
  .blurb p + p { margin-top: 16px; }
  .back-motif {
    position: absolute;
    left: 150px;
    bottom: -90px;
    width: 300px;
    height: 340px;
    border-radius: 50%;
    background: radial-gradient(circle, rgba(255,255,255,0.10), rgba(255,255,255,0.02) 70%);
  }

  /* Spine */
  .spine {
    width: 36px;
    height: 100%;
    background: var(--spine-green);
    display: flex;
    align-items: center;
    justify-content: center;
  }
  .spine-title {
    writing-mode: vertical-rl;
    font-family: "Anton", sans-serif;
    font-size: 15px;
    letter-spacing: 0.5px;
    color: var(--paper);
    text-transform: uppercase;
    white-space: nowrap;
  }

  /* Front cover */
  .front-cover {
    position: relative;
    width: 520px;
    height: 100%;
    background: radial-gradient(ellipse 60% 50% at 50% 38%, var(--green-light) 0%, var(--green-mid) 55%, var(--green-deep) 100%);
    overflow: hidden;
  }
  .author {
    position: absolute;
    top: 52px;
    left: 0;
    right: 0;
    text-align: center;
    font-weight: 800;
    font-size: 22px;
    color: var(--ink-dark);
  }
  .bulb-art {
    position: absolute;
    top: 110px;
    left: 140px;
    width: 240px;
    height: 240px;
  }
  .title {
    position: absolute;
    left: 0;
    right: 0;
    top: 400px;
    text-align: center;
    font-family: "Anton", sans-serif;
    font-weight: 400;
    color: var(--paper);
    text-transform: uppercase;
    line-height: 1.05;
  }
  .title-lead { display: block; font-size: 30px; margin-bottom: 8px; letter-spacing: 0.5px; }
  .title-main { display: block; font-size: 50px; letter-spacing: 0.5px; }
</style>
</head>
<body>
  <div class="cover-wrap">
    <section class="back-cover">
      <div class="publisher-mark">
        <span class="publisher-square"></span>
        <span class="publisher-name">Larchmoor Tax Studio</span>
      </div>
      <div class="blurb">
        <p>The music industry is shapeshifting. Music artists must work harder than ever to make a career of their creative mastery. As an artist you are not in a typical profession but you can be big business. A good business mindset starts with ensuring you understand that you are a business and that you will need the right team on board to help you navigate the legal complexities of the business world.</p>
        <p>Whilst you may have a first rate attack in terms of your manager and record label, success won't be guaranteed unless you have a first rate line of defense to help protect your earnings. This book provides an easy-to-understand overview of setting up in business for the first time, some practical tips on getting started, as well as a discussion of the business challenges you'll face along your journey to becoming an international superstar.</p>
      </div>
      <div class="back-motif" role="img" aria-label="Faint large light bulb line drawing"></div>
    </section>

    <div class="spine">
      <span class="spine-title">The Stage Performer: A Working Handbook for Launching Your Trade</span>
    </div>

    <section class="front-cover">
      <div class="author">Gareth L. Quinby</div>
      <svg class="bulb-art" viewBox="0 0 240 240" role="img" aria-label="Glowing yellow light bulb illustration with rays">
        <defs>
          <radialGradient id="bulbGlow" cx="50%" cy="50%" r="50%">
            <stop offset="0%" stop-color="#f2e600" stop-opacity="0.9"/>
            <stop offset="60%" stop-color="#e6de2a" stop-opacity="0.4"/>
            <stop offset="100%" stop-color="#e6de2a" stop-opacity="0"/>
          </radialGradient>
        </defs>
        <circle cx="120" cy="120" r="120" fill="url(#bulbGlow)"/>
      </svg>
      <h1 class="title">
        <span class="title-lead">The Stage Performer:</span>
        <span class="title-main">A Working Handbook<br>for Launching<br>Your Trade</span>
      </h1>
    </section>
  </div>
</body>
</html>
```